Business Cards

I'd like help creating business cards with the full logo "Veltrona Capital Partners" on the back of the card (navy background with white writing), and abbreviated logo "VCP" on the front. Would like to list name, title, phone number, email, and website listed on front of card. Would like to keep very simple. Front font Arial or similar.

```html
<!DOCTYPE html>
<html lang="en">
<head>
<meta charset="utf-8">
<title>Veltrona Capital Partners – Business Cards</title>
<link rel="stylesheet" href="https://fonts.googleapis.com/css2?family=Montserrat:wght@400;600;700&display=swap">
<style>
  :root {
    --navy: #1c3668;
    --navy-deep: #1c3668;
    --ink-grey: #5e5e5e;
    --paper: #ffffff;
    --backdrop: #b3b3b3;
  }
  * { box-sizing: border-box; margin: 0; padding: 0; }
  html, body {
    width: 1182px;
    height: 1200px;
    overflow: hidden;
    background: var(--backdrop);
    font-family: "Montserrat", Arial, sans-serif;
  }
  .canvas {
    position: relative;
    width: 1182px;
    height: 1200px;
  }
  .card {
    position: absolute;
    left: 266px;
    width: 649px;
    height: 371px;
  }
  .card--front {
    top: 156px;
    background: var(--paper);
  }
  .card--back {
    top: 645px;
    background: var(--navy-deep);
    display: flex;
    align-items: center;
    justify-content: center;
  }

  /* Front */
  .holder {
    position: absolute;
    left: 41px;
    top: 34px;
  }
  .holder__name {
    font-weight: 700;
    font-size: 25px;
    line-height: 1.1;
    color: var(--navy);
  }
  .holder__title {
    font-weight: 600;
    font-size: 17px;
    line-height: 1.2;
    color: var(--ink-grey);
    margin-top: 2px;
  }
  .monogram {
    position: absolute;
    left: 50%;
    top: 185px;
    transform: translate(-50%, -50%);
    display: flex;
    align-items: center;
    gap: 10px;
  }
  .monogram__square {
    width: 14px;
    height: 14px;
    background: var(--navy);
  }
  .monogram__text {
    font-weight: 700;
    font-size: 54px;
    letter-spacing: 1px;
    color: var(--navy);
    line-height: 1;
  }
  .contact {
    position: absolute;
    left: 39px;
    top: 298px;
    font-size: 16px;
    line-height: 21px;
    color: var(--ink-grey);
    list-style: none;
  }
  .contact__label {
    display: inline-block;
    width: 26px;
    font-weight: 600;
    color: var(--navy);
  }
  .website {
    position: absolute;
    left: 609px;
    top: 185px;
    transform: translate(-50%, -50%) rotate(90deg);
    font-size: 17px;
    color: var(--navy);
    white-space: nowrap;
  }

  /* Back */
  .wordmark {
    display: flex;
    flex-direction: column;
    align-items: center;
    color: var(--paper);
    font-weight: 600;
    margin-top: -8px;
  }
  .wordmark__main {
    font-size: 50px;
    letter-spacing: 2px;
    line-height: 1;
  }
  .wordmark__sub {
    font-size: 18px;
    letter-spacing: 9px;
    margin-top: 14px;
    margin-right: -9px;
    line-height: 1;
  }
</style>
</head>
<body>
  <main class="canvas">
    <section class="card card--front" aria-label="Business card front">
      <div class="holder">
        <p class="holder__name">List Name</p>
        <p class="holder__title">Title</p>
      </div>

      <div class="monogram">
        <span class="monogram__square" aria-hidden="true"></span>
        <span class="monogram__text">VCP</span>
      </div>

      <ul class="contact">
        <li><span class="contact__label">P:</span>123 456 789</li>
        <li><span class="contact__label">E:</span>email@veltronacp.com</li>
      </ul>

      <p class="website">www.veltronacp.com</p>
    </section>

    <section class="card card--back" aria-label="Business card back">
      <div class="wordmark">
        <span class="wordmark__main">VELTRONA</span>
        <span class="wordmark__sub">CAPITAL PARTNERS</span>
      </div>
    </section>
  </main>
</body>
</html>
```